Political Marketing company needs a Valentine's Day Card - Mirror Benske

We need a 5"x7" Valentine's Day card in the style of the attached images. We want it to be slightly cartoon-y, but heartfelt. Copy for card is as follows, with creative direction in parenthesis - line breaks are indicated by forward slash: Outside: This Valentine’s Day, / I want to tell you / something special… (serif clean font - darker background, light colored font) Inside: I love you / more than / Benske loves Benske! (graphic of Harold Benske looking at himself in the mirror)

```html
<!DOCTYPE html>
<html lang="en">
<head>
<meta charset="utf-8">
<title>Valentine's Day Card – Benske</title>
<link rel="stylesheet" href="https://fonts.googleapis.com/css2?family=Nunito:wght@800;900&display=swap">
<style>
  :root {
    --backdrop: #f9e4c1;
    --card-light: #fdf3d6;
    --card-mid: #f6dc96;
    --card-deep: #eec25a;
    --band: #e3b553;
    --ink-brown: #a8661a;
    --ink-white: #ffffff;
    --art-gold: #e6bd68;
    --art-amber: #c99447;
    --art-navy: #3f4a70;
    --card-edge: rgba(150, 100, 30, 0.25);
  }
  * { box-sizing: border-box; margin: 0; padding: 0; }
  html, body {
    width: 1200px;
    height: 696px;
    overflow: hidden;
    background: var(--backdrop);
    font-family: "Nunito", "Arial Rounded MT Bold", sans-serif;
  }
  .spread {
    width: 1200px;
    height: 696px;
    display: flex;
    justify-content: center;
    align-items: center;
    gap: 60px;
  }
  .card {
    position: relative;
    width: 520px;
    height: 372px;
    border: 1px solid var(--card-edge);
    box-shadow: 0 6px 18px rgba(120, 80, 20, 0.18);
    overflow: hidden;
  }
  .card--outside {
    background: radial-gradient(ellipse at 48% 55%, var(--card-light) 0%, var(--card-mid) 62%, var(--card-deep) 100%);
    display: flex;
    align-items: center;
    justify-content: center;
  }
  .outside-message {
    color: var(--ink-brown);
    font-weight: 900;
    font-size: 42px;
    line-height: 1.14;
    text-align: center;
  }
  .card--inside {
    background: linear-gradient(160deg, var(--card-deep) 0%, var(--card-light) 55%, var(--card-mid) 100%);
  }
  .inside-band {
    position: absolute;
    top: 24px;
    left: 0;
    width: 100%;
    height: 108px;
    background: var(--band);
    display: flex;
    align-items: center;
    justify-content: center;
  }
  .inside-message {
    color: var(--ink-white);
    font-weight: 900;
    font-size: 38px;
    line-height: 1.12;
    text-align: center;
  }
  .inside-art {
    position: absolute;
    left: 120px;
    top: 146px;
    width: 340px;
    height: 214px;
    border-radius: 46px;
    background:
      radial-gradient(ellipse at 70% 30%, rgba(255, 240, 200, 0.45) 0%, rgba(255, 240, 200, 0) 55%),
      linear-gradient(135deg, var(--art-gold) 0%, var(--art-amber) 55%, var(--art-navy) 100%);
  }
</style>
</head>
<body>
  <main class="spread">
    <section class="card card--outside" aria-label="Card outside">
      <p class="outside-message">This Valentine’s Day,<br>I want to tell you<br>something special…</p>
    </section>

    <section class="card card--inside" aria-label="Card inside">
      <div class="inside-band">
        <p class="inside-message">I love you / more than<br>Benske loves Benske!</p>
      </div>
      <div class="inside-art" role="img"
           aria-label="Cartoon illustration of Harold Benske admiring his reflection in an ornate gold mirror against striped wallpaper"></div>
    </section>
  </main>
</body>
</html>
```